hi-tech exotic coatings company needs a business card

we need a business card design for a new company based in South Florida called TRV GROUP LLC. trv stands for "thermal vapor reinforcing" we have a proprietary process to diffuse metallic elements from the periodic table of elements into and onto industrial or medical critical components ie gas turbine blades, prosthetic implants such as a prosthetic hip or chemical processing components .The end result is a coating or a diffusion of exotic alloys with exotic surface properties on our customers parts. BUT WE DON'T SELL COATINGS we enter into a joint venture or licence agreement if we solve the problem.We would like a slogan on the front ? something like " EXTENDING THE LIFE OR YOUR CRITICAL COMPONENTS" by itself or WITH SCIENCE or WITH TECHNOLOGY.or a better slogan.
Updates
slogan we would like to see on cards in small
Industry/Entity Type
Business

```html
<!DOCTYPE html>
<html lang="en">
<head>
<meta charset="utf-8">
<title>TRV Group LLC – Business Card</title>
<link rel="stylesheet" href="https://fonts.googleapis.com/css2?family=Open+Sans:wght@400;600&family=Michroma&display=swap">
<style>
  :root {
    --backdrop: #3b2618;
    --front-deep: #0a3f9c;
    --front-mid: #0d56c8;
    --front-glow: #1f78e6;
    --white: #ffffff;
    --navy: #1b2a6b;
    --navy-soft: #2a3a80;
  }
  html, body {
    margin: 0;
    padding: 0;
    width: 1200px;
    height: 1000px;
    overflow: hidden;
    background: var(--backdrop);
    font-family: "Open Sans", Arial, sans-serif;
  }
  .canvas {
    position: relative;
    width: 1200px;
    height: 1000px;
  }
  .card {
    position: absolute;
    top: 315px;
    width: 561px;
    height: 320px;
    box-shadow: 0 6px 14px rgba(0,0,0,0.45);
    overflow: hidden;
  }
  .card-front {
    left: 33px;
    background:
      radial-gradient(ellipse at 20% 85%, var(--front-glow) 0%, rgba(31,120,230,0) 55%),
      radial-gradient(ellipse at 70% 10%, var(--front-mid) 0%, rgba(13,86,200,0) 60%),
      linear-gradient(135deg, var(--front-mid) 0%, var(--front-deep) 100%);
    color: var(--white);
  }
  .card-back {
    left: 619px;
    background: var(--white);
    color: var(--navy);
  }
  .rule {
    position: absolute;
    height: 0;
    border-top: 1.5px solid currentColor;
  }
  .card-front .rule { left: 80px; width: 398px; }
  .card-front .rule-top { top: 55px; }
  .card-front .rule-bottom { top: 171px; }
  .card-back .rule { left: 148px; width: 263px; border-top-width: 1px; }
  .card-back .rule-top { top: 37px; }
  .card-back .rule-bottom { top: 114px; }
  .centered {
    position: absolute;
    left: 0;
    right: 0;
    text-align: center;
    margin: 0;
  }
  .brand-name {
    font-weight: 600;
    letter-spacing: 6px;
  }
  .card-front .brand-name { top: 66px; font-size: 48px; line-height: 60px; }
  .card-back .brand-name { top: 42px; font-size: 31px; line-height: 40px; }
  .company-line { font-weight: 400; white-space: nowrap; }
  .card-front .company-line { top: 134px; font-size: 19px; }
  .card-back .company-line { top: 89px; font-size: 12px; }
  .slogan {
    top: 227px;
    font-size: 17px;
    line-height: 21px;
  }
  .person-name {
    top: 144px;
    font-family: "Michroma", "Open Sans", sans-serif;
    font-size: 18px;
    letter-spacing: 2px;
  }
  .person-role {
    top: 170px;
    font-size: 12.5px;
    letter-spacing: 1px;
    color: var(--navy-soft);
  }
  .contact-list {
    top: 204px;
    font-size: 13px;
    line-height: 17.5px;
    list-style: none;
    padding: 0;
  }
</style>
</head>
<body>
<main class="canvas">
  <section class="card card-front" aria-label="Card front">
    <div class="rule rule-top"></div>
    <p class="centered brand-name">TRV</p>
    <p class="centered company-line">THERMAL VAPOR REINFORCING GROUP LLC</p>
    <div class="rule rule-bottom"></div>
    <p class="centered slogan">Adding Years to the Parts Your Operation Relies On<br>through Research and Precision</p>
  </section>

  <section class="card card-back" aria-label="Card back">
    <div class="rule rule-top"></div>
    <p class="centered brand-name">TRV</p>
    <p class="centered company-line">THERMAL VAPOR REINFORCING GROUP LLC</p>
    <div class="rule rule-bottom"></div>
    <p class="centered person-name">JOHN SMITH</p>
    <p class="centered person-role">POSITION</p>
    <ul class="centered contact-list">
      <li>P:&nbsp; 123.456.7890</li>
      <li>M:&nbsp; 123.456.7891</li>
      <li>E:&nbsp; JOHN@TRVGROUPLLC.COM</li>
      <li>WWW.TRVGROUPLLC.COM</li>
    </ul>
  </section>
</main>
</body>
</html>
```